TrekLinkway Impact Flyer

TrekLinkway needs a 1 page flyer to bring to meetings with policy makers and industry partners that clearly communicates the value and impacts of our organization.

TrekLinkway is a coalition of twelve Transportation Management Associations (TMAs) working with over 300 businesses, medical facilities, property managers, land developers and higher learning institutions in 39 municipalities across the Commonwealth to improve and increase transportation choices for commuters. TMAs leverage public and private funds to promote and provide transportation options which reduce traffic congestion and vehicle emissions while improving access to employment destinations and quality of life for commuters.

The flyer will be accompanied by an infographic we have already prepared so the goal of this piece is to present the text we have written in a visually pleasing and effective way. This text will be complete this afternoon!

Target Market(s)

Legislators, municipal leaders and staff, policy makers, business owners. People who probably have no knowledge of who we are and what we do, but who we want to work with and to have their support.

Industry/Entity Type

Industry

Font styles to use
Serif
Other font styles liked:
• Bendor, Edmonsans, Governor

Colors
00a88f
86cfc6
cadf82
e9f1ce

Requirements
Must have
• Must be 1 page, include TrekLinkway logo and, space permitting, the infographic (this can also be a separate page but would be nice to include it somehow on the 1 pager
Nice to have
• pop outs to distinguish different sections of the text

```html
<!DOCTYPE html>
<html lang="en">
<head>
<meta charset="utf-8">
<title>TrekLinkway – Getting You There</title>
<link rel="stylesheet" href="https://fonts.googleapis.com/css2?family=Arvo:wght@700&family=Crimson+Text:wght@400;600&family=Josefin+Sans:wght@400&display=swap">
<style>
  :root {
    --paper: #f8f0c6;
    --teal: #00a88f;
    --lime: #cadf82;
    --lime-pale: #f3f6dc;
    --card-green: #c5da86;
    --banner: #6f9e88;
    --ink: #1d1d1b;
    --marker: #e2542a;
    --white: #ffffff;
    --serif: "Crimson Text", Georgia, serif;
    --slab: "Arvo", Georgia, serif;
    --display: "Josefin Sans", Arial, sans-serif;
  }
  * { box-sizing: border-box; margin: 0; padding: 0; }
  html, body { width: 1200px; height: 848px; overflow: hidden; background: var(--paper); }
  .flyer { position: relative; width: 1200px; height: 848px; overflow: hidden; background: var(--paper); font-family: var(--serif); color: var(--ink); }

  .road-area { position: absolute; background: var(--lime); opacity: .55; }

  .masthead { position: absolute; left: 60px; top: 33px; width: 548px; height: 150px; background: var(--white); border: 2px solid var(--ink); border-radius: 18px; }
  .masthead__banner { position: absolute; left: 10px; top: 12px; width: 528px; height: 104px; background: var(--banner); display: flex; align-items: center; padding-left: 143px; }
  .masthead__tagline { font-family: var(--display); color: var(--white); font-size: 30px; letter-spacing: 2.5px; text-transform: uppercase; white-space: nowrap; padding-top: 6px; }
  .brand { position: absolute; left: 2px; top: 3px; width: 138px; height: 140px; border-radius: 50%; background: var(--ink); display: flex; align-items: center; justify-content: center; }
  .brand__name { font-family: var(--serif); font-weight: 600; font-size: 21px; color: var(--white); }

  .section-title { position: absolute; font-family: var(--slab); font-size: 16px; color: var(--ink); display: flex; align-items: center; gap: 3px; white-space: nowrap; }
  .section-title::before { content: ""; width: 11px; height: 13px; background: var(--marker); border-radius: 50% 50% 50% 0; }

  .text-box { position: absolute; background: var(--white); border-radius: 12px; font-size: 13.4px; line-height: 1.28; padding: 6px 14px; }

  .audiences { position: absolute; left: 48px; top: 522px; display: flex; gap: 10px; }
  .audience { height: 226px; border-radius: 14px; padding: 52px 8px 0; text-align: center; font-size: 13.4px; line-height: 1.3; position: relative; }
  .audience--green { background: var(--card-green); }
  .audience--pale { background: var(--lime-pale); border: 2px solid var(--card-green); }
  .audience__label { position: absolute; left: 14px; right: 14px; top: 18px; background: var(--lime-pale); border: 1px solid var(--card-green); font-family: var(--slab); font-size: 12.5px; padding: 3px 0; text-align: center; }
  .audience--pale .audience__label { background: var(--white); }

  .impact-graphic { position: absolute; left: 748px; top: 40px; width: 400px; height: 446px; border: 1px solid #c9c3a0; background: linear-gradient(180deg, #b7d8e6 0%, #a5cc5a 22%, #9ac44f 100%); }
  .trees-area { position: absolute; left: 662px; top: 195px; width: 84px; height: 280px; background: linear-gradient(180deg, #4e8a5a, #3c6e47); opacity: .8; }
  .grass { position: absolute; left: 36px; top: 756px; width: 624px; height: 44px; background: linear-gradient(180deg, rgba(160,200,90,.15), #a7cc62); }

  .members-title { position: absolute; left: 800px; top: 642px; font-family: var(--slab); font-size: 15px; color: var(--teal); white-space: nowrap; }
  .members { position: absolute; left: 783px; top: 664px; display: grid; grid-template-columns: 220px 180px; font-size: 13.4px; line-height: 1.3; list-style: none; }
</style>
</head>
<body>
<div class="flyer">
  <header class="masthead">
    <div class="masthead__banner"><span class="masthead__tagline">Getting You There</span></div>
    <div class="brand"><span class="brand__name">TrekLinkway</span></div>
  </header>

  <h2 class="section-title" style="left:78px;top:204px">Who is TrekLinkway?</h2>
  <p class="text-box" style="left:70px;top:229px;width:532px">TrekLinkway is a coalition of twelve Transportation Management Associations (TMAs) working with over 300 businesses, medical facilities, property managers, land developers and higher learning institutions in 39 municipalities across the Commonwealth to improve and increase transportation choices for commuters. With a mission to Collaborate, Advocate, and Inform, TrekLinkway provides a platform for Massachusetts TMAs to work together and with state agencies to support projects that reduce traffic congestion, improve air quality and expand access to employment destinations.</p>

  <h2 class="section-title" style="left:84px;top:373px">What are TMAs?</h2>
  <p class="text-box" style="left:75px;top:402px;width:548px">Transportation Management Associations (TMAs) are non-profit organizations that leverage public and private funds to provide transportation options (like shuttles and vanpools) that decrease drive alone commuting and improve both workplace satisfaction and quality of life for commuters.</p>

  <h2 class="section-title" style="left:242px;top:485px">TrekLinkway works for...</h2>

  <div class="audiences">
    <section class="audience audience--green" style="width:150px"><h3 class="audience__label">Government</h3>
      <p>Our TMAs work with municipalities to address transportation issues at the local level and convene diverse stakeholders around common goals of traffic reduction and sustained economic growth.</p></section>
    <section class="audience audience--pale" style="width:190px"><h3 class="audience__label">Businesses</h3>
      <p>By pooling resources from multiple businesses, TMAs both relieve employers from the burden of providing commuter options programs and significantly reduce the costs of participating in these programs that benefit their employees.</p></section>
    <section class="audience audience--green" style="width:136px"><h3 class="audience__label">Employees</h3>
      <p>TrekLinkway TMAs help employees develop personalized commuter assistance plans that save time and money and earn rewards for choosing a greener commute.</p></section>
    <section class="audience audience--pale" style="width:128px"><h3 class="audience__label">Residents</h3>
      <p>All TMA shuttles are open to the public and alleviate local traffic congestion and clear the air by taking cars off the road.</p></section>
  </div>

  <div class="impact-graphic" role="img" aria-label="Infographic: The impact of TMAs in 2013 — gallons of gas saved, annual shuttle boardings, vehicle trips and CO2 reduced, employees served and dollars saved by commuters, shown along a winding road through green hills"></div>
  <div class="trees-area" role="img" aria-label="Illustration of two pine trees"></div>
  <div class="grass" role="img" aria-label="Illustration of a row of grass tufts"></div>

  <h2 class="section-title" style="left:795px;top:513px">Support TrekLinkway!</h2>
  <p class="text-box" style="left:785px;top:540px;width:330px">By reducing congestion and creating policies that help meet statewide goals for mode shift, public health, and environmental quality, we are making Massachusetts a better place to live, work and do business;</p>

  <h3 class="members-title">TrekLinkway TMA Members Include:</h3>
  <ul class="members">
    <li>Elmfield Medical Group</li><li>Keystone Assurance</li>
    <li>Northgate General Hospital</li><li>Brightline Energy</li>
    <li>City of Harborview</li><li>Bayfield University</li>
  </ul>
</div>
</body>
</html>
```